Energieberatung sucht Corporate Design
Zielgruppe
Ich führe Energieberatungen für Immobilieneigentümer durch, erstelle Sanierungsvorschläge sowie Förderanträge. Für Verkäufer und Vermieter fertige ich Energieausweise an, um die energetisch Qualität des Gebäudes darzustellen.
Energieberatung soll für die Kunden ein Wegweiser für modernes, klimaneutrales und kostengünstiges Wohnen sein.
Meine Zielgruppe sind Immobilieneigentümer, Verkäufer und Vermieter von Immobilien sowie Käufer von Immobilien.
Aufgabenstellung
Ich suche ein hochwertiges Design, welches modern und zeitlos ist, aber auch die energetische Komponente berücksichtigt. Mit dem Design soll das verstaubte Image der Energieberatung abgelegt werden. Die Kunden sollen damit zukunftsorientiertes, modernes Wohnen, Wohnqualität und Kostenersparnis verbinden.

```html
<!DOCTYPE html>
<html lang="de">
<head>
<meta charset="utf-8">
<title>Energieberatung Lena Voss – Geschäftsausstattung</title>
<link rel="stylesheet" href="https://fonts.googleapis.com/css2?family=Inter:wght@400;500;600&display=swap">
<style>
:root{
  --board:#9ba1ab;
  --paper:#ffffff;
  --teal:#117896;
  --ink:#4a4a4a;
  --grey:#7d7d7d;
  --faint:#eceded;
  --yellow:#f2c400;
  --black:#1a1a1a;
}
*{box-sizing:border-box;margin:0;padding:0}
html,body{width:1000px;height:1200px;overflow:hidden}
body{background:var(--board);font-family:"Inter",Arial,sans-serif;position:relative;color:var(--ink)}
.sheet{position:absolute;background:var(--paper);box-shadow:3px 4px 10px rgba(0,0,0,.25)}
.brand{position:absolute;display:flex;align-items:center;gap:10px}
.brand-mark{background:var(--teal);flex:none}
.brand-name{color:var(--teal);font-weight:600;letter-spacing:.12em;text-transform:uppercase;line-height:1.25}
.brand--black .brand-mark{background:var(--black)}
.brand--black .brand-name{color:var(--black)}
.contact{list-style:none;font-size:6.6px;line-height:9.7px;color:var(--ink)}
.contact li{display:flex;align-items:center;gap:5px}
.contact svg{width:6px;height:6px;fill:var(--teal);flex:none}
.hl{color:var(--teal)}
.bar{position:absolute;background:var(--teal)}
/* presentation card */
.card-large{left:55px;top:28px;width:488px;height:263px}
.card-paper{left:565px;top:28px;width:375px;height:264px;background:#f4f4f2}
/* business card */
.bc-front{left:56px;top:341px;width:235px;height:152px}
.bc-role{position:absolute;left:17px;top:73px;font-size:7.6px}
.bc-address{position:absolute;left:17px;top:102px;font-size:6.6px;line-height:9.7px}
.bc-divider{position:absolute;left:121px;top:100px;width:1px;height:44px;background:var(--teal)}
.bc-front .contact{position:absolute;left:130px;top:101px}
.bc-back{left:56px;top:508px;width:235px;height:151px;background:var(--teal)}
.bc-back-mark{position:absolute;left:99px;top:48px;width:36px;height:36px;background:var(--yellow)}
.bc-url{position:absolute;left:0;right:0;top:99px;text-align:center;color:var(--yellow);font-size:9px;font-weight:600;letter-spacing:.04em}
/* envelope */
.envelope{left:54px;top:840px;width:500px;height:237px;z-index:2;box-shadow:2px 3px 8px rgba(0,0,0,.3)}
/* letterhead */
.letterhead{left:364px;top:339px;width:579px;height:820px}
.lh-sender{position:absolute;left:60px;top:125px;font-size:6.4px}
.lh-contact{position:absolute;left:419px;top:95px}
.fold{position:absolute;left:0;height:1px;background:#bdbdbd}
.lh-watermark{position:absolute;left:95px;top:240px;width:396px;height:380px;background:var(--faint)}
.lh-footer{position:absolute;left:60px;top:772px;display:flex;font-size:6.6px;line-height:10.5px}
.lh-footer .col{padding:0 8px;border-left:1px solid var(--teal);height:36px}
.lh-footer .col:first-child{padding-left:0;border-left:none}
.lh-footer .contact{font-size:6.6px;line-height:10px}
</style>
</head>
<body>

<section class="sheet card-large">
  <div class="brand" style="left:105px;top:100px">
    <span class="brand-mark" style="width:58px;height:58px"></span>
    <span class="brand-name" style="font-size:15px">Energieberatung<br>Lena Voss</span>
  </div>
</section>

<section class="sheet card-paper">
  <div class="brand" style="left:72px;top:100px">
    <span class="brand-mark" style="width:48px;height:48px"></span>
    <span class="brand-name" style="font-size:13px">Energieberatung<br>Lena Voss</span>
  </div>
</section>

<section class="sheet bc-front">
  <div class="brand" style="left:17px;top:16px">
    <span class="brand-mark" style="width:28px;height:28px"></span>
    <span class="brand-name" style="font-size:7.6px">Energieberatung<br>Lena Voss</span>
  </div>
  <p class="bc-role"><span class="hl">Lena Voss</span> - Geschäftsführung</p>
  <p class="bc-address">Musterstraße 126<br>00000 Musterstadt</p>
  <span class="bc-divider"></span>
  <ul class="contact">
    <li><svg viewBox="0 0 10 10"><path d="M2 0l2 2-1 1.5c.8 1.6 1.9 2.7 3.5 3.5L8 6l2 2-1.5 2C4 9.5.5 6 0 1.5z"/></svg>+49 1234-56789-0</li>
    <li><svg viewBox="0 0 10 10"><path d="M2 0h6v3H2zM0 3.5h10v4.5H8v2H2V8H0z"/></svg>+49 1234-56789-1</li>
    <li><svg viewBox="0 0 10 10"><path d="M0 2h10v6H0zM0 2l5 3.5L10 2"/></svg>info@energie-voss.de</li>
    <li><svg viewBox="0 0 10 10"><circle cx="5" cy="5" r="5"/></svg>www.energie-voss.de</li>
  </ul>
  <span class="bar" style="left:16px;bottom:0;width:202px;height:8px"></span>
</section>

<section class="sheet bc-back">
  <span class="bc-back-mark"></span>
  <p class="bc-url">www.energie-voss.de</p>
</section>

<div class="brand brand--black" style="left:63px;top:727px">
  <span class="brand-mark" style="width:48px;height:48px"></span>
  <span class="brand-name" style="font-size:11px">Energieberatung<br>Lena Voss</span>
</div>

<section class="sheet letterhead">
  <div class="brand" style="left:369px;top:37px">
    <span class="brand-mark" style="width:38px;height:38px"></span>
    <span class="brand-name" style="font-size:9px">Energieberatung<br>Lena Voss</span>
  </div>
  <ul class="contact lh-contact">
    <li><svg viewBox="0 0 10 10"><path d="M2 0l2 2-1 1.5c.8 1.6 1.9 2.7 3.5 3.5L8 6l2 2-1.5 2C4 9.5.5 6 0 1.5z"/></svg>+49 1234-56789-0</li>
    <li><svg viewBox="0 0 10 10"><path d="M2 0h6v3H2zM0 3.5h10v4.5H8v2H2V8H0z"/></svg>+49 1234-56789-1</li>
    <li><svg viewBox="0 0 10 10"><path d="M0 2h10v6H0zM0 2l5 3.5L10 2"/></svg>info@energie-voss.de</li>
    <li><svg viewBox="0 0 10 10"><circle cx="5" cy="5" r="5"/></svg>www.energie-voss.de</li>
  </ul>
  <p class="lh-sender"><span class="hl">Energieberatung Lena Voss</span> - Postfach 0000 - 00000 Musterstadt</p>
  <span class="fold" style="top:242px;width:20px"></span>
  <span class="fold" style="top:413px;width:28px"></span>
  <span class="lh-watermark"></span>
  <footer class="lh-footer">
    <div class="col"><span class="hl">Energieberatung Lena Voss</span><br>Musterstraße 126<br>00000 Musterstadt</div>
    <div class="col"><span class="hl">Geschäftsführung</span><br>Lena Voss</div>
    <div class="col">
      <ul class="contact">
        <li><svg viewBox="0 0 10 10"><path d="M2 0l2 2-1 1.5c.8 1.6 1.9 2.7 3.5 3.5L8 6l2 2-1.5 2C4 9.5.5 6 0 1.5z"/></svg>+49 1234-56789-0</li>
        <li><svg viewBox="0 0 10 10"><path d="M2 0h6v3H2zM0 3.5h10v4.5H8v2H2V8H0z"/></svg>+49 1234-56789-1</li>
        <li><svg viewBox="0 0 10 10"><circle cx="5" cy="5" r="5"/></svg>www.energie-voss.de</li>
      </ul>
    </div>
    <div class="col"><span class="hl">Amtsgericht Stadt</span><br>ABC 0000XX<br>UST-ID DE 000XX</div>
    <div class="col"><span class="hl">Bankverbindung ABC</span><br>IBAN DE12 3456 7890 1234 5678<br>BIC ABCDEF12345</div>
  </footer>
  <span class="bar" style="left:59px;top:810px;width:479px;height:10px"></span>
</section>

<section class="sheet envelope">
  <div class="brand" style="left:28px;top:30px">
    <span class="brand-mark" style="width:38px;height:38px"></span>
    <span class="brand-name" style="font-size:9px">Energieberatung<br>Lena Voss</span>
  </div>
</section>

</body>
</html>
```